Wordpress Theme Design for Teaching English

I am an English tutor in Hong Kong and this website is to advertise my services and provide teaching materials

```html
<!DOCTYPE html>
<html lang="en">
<head>
<meta charset="utf-8">
<title>Learn English Today</title>
<link rel="stylesheet" href="https://fonts.googleapis.com/css2?family=PT+Sans:ital,wght@1,400&family=Arimo:wght@400;700&family=Noto+Sans:wght@400;700&display=swap">
<style>
  :root {
    --green-bright: #8cc63f;
    --green-light: #b5dc6e;
    --green-pale: #eaf5d8;
    --green-dark: #1f5a14;
    --green-deep: #2f6a1b;
    --link-green: #7cb82f;
    --ink: #111111;
    --muted: #555555;
    --rule: #c9e29c;
    --white: #ffffff;
  }
  * { box-sizing: border-box; margin: 0; padding: 0; }
  html, body {
    width: 1158px;
    height: 1200px;
    overflow: hidden;
    background: var(--white);
  }
  .page {
    position: relative;
    width: 1158px;
    height: 1200px;
    overflow: hidden;
    font-family: "Noto Sans", Tahoma, sans-serif;
    color: var(--ink);
  }

  /* Hero artwork area */
  .hero-art {
    position: absolute;
    left: 0;
    top: 0;
    width: 1158px;
    height: 750px;
    background:
      radial-gradient(ellipse 520px 260px at 380px 470px, rgba(31,90,20,0.55), rgba(31,90,20,0) 70%),
      radial-gradient(ellipse 480px 300px at 850px 300px, rgba(140,198,63,0.6), rgba(140,198,63,0) 72%),
      radial-gradient(ellipse 300px 200px at 220px 330px, rgba(17,17,17,0.25), rgba(17,17,17,0) 70%),
      linear-gradient(180deg, var(--white) 0%, var(--green-pale) 55%, var(--white) 100%);
  }

  /* Navigation */
  .main-nav {
    position: absolute;
    left: 444px;
    top: 18px;
    width: 714px;
    height: 54px;
    background: linear-gradient(180deg, #9ed34f 0%, var(--green-bright) 100%);
    border-radius: 6px 0 0 6px;
    display: flex;
    align-items: center;
    justify-content: space-between;
    padding: 0 12px 0 26px;
  }
  .main-nav a {
    display: flex;
    align-items: center;
    gap: 14px;
    font-family: "PT Sans", "Myriad Pro", sans-serif;
    font-style: italic;
    font-size: 22px;
    color: var(--white);
    text-decoration: none;
  }
  .main-nav svg { width: 13px; height: 10px; }

  /* Content columns */
  .column {
    position: absolute;
    font-size: 12.5px;
    line-height: 15.5px;
  }
  .column h2 {
    font-family: "Arimo", Arial, sans-serif;
    font-weight: 700;
    font-size: 20px;
    color: var(--green-dark);
    padding-bottom: 12px;
    border-bottom: 1px solid var(--rule);
    margin-bottom: 14px;
  }
  .column p { margin-bottom: 12px; }
  .column .lead { font-weight: 700; display: block; }
  .column a { color: var(--link-green); }

  .column--learn { left: 44px; top: 791px; width: 354px; }
  .column--about { left: 434px; top: 791px; width: 354px; }

  .column--news { left: 844px; top: 767px; width: 292px; }
  .column--news h2 { padding-bottom: 12px; margin-bottom: 12px; }
  .news-item { padding-left: 24px; margin-bottom: 12px; }
  .news-item time {
    display: block;
    font-family: "Arimo", Arial, sans-serif;
    font-weight: 700;
    font-size: 13px;
    color: var(--link-green);
    margin-bottom: 14px;
  }
  .news-item p { margin-bottom: 6px; }
  .news-item a { font-weight: 700; }
  .read-more {
    display: block;
    text-align: right;
    font-weight: 700;
    font-size: 12.5px;
  }

  /* Footer */
  .site-footer {
    position: absolute;
    left: 0;
    top: 1095px;
    width: 1158px;
    height: 105px;
    background: linear-gradient(90deg, var(--green-pale) 0%, #f6fbee 28%, var(--white) 45%);
  }
  .footer-copy {
    position: absolute;
    left: 84px;
    top: 32px;
    font-size: 12.5px;
    color: var(--muted);
  }
  .footer-links {
    position: absolute;
    left: 89px;
    top: 58px;
    font-family: "Arimo", Arial, sans-serif;
    font-weight: 700;
    font-size: 13px;
    color: var(--deep, var(--green-deep));
  }
  .footer-links a { color: var(--green-deep); }
  .footer-art {
    position: absolute;
    left: 515px;
    top: 5px;
    width: 553px;
    height: 100px;
    background:
      radial-gradient(ellipse 260px 90px at 50% 100%, rgba(31,90,20,0.45), rgba(31,90,20,0) 75%),
      radial-gradient(ellipse 120px 70px at 85% 90%, rgba(17,17,17,0.25), rgba(17,17,17,0) 75%);
  }
</style>
</head>
<body>
<div class="page">

  <div class="hero-art" role="img" aria-label="Decorative flowing swirl illustration in light green, dark green and black, with dots and curls sweeping across the header"></div>

  <nav class="main-nav">
    <a href="#"><svg viewBox="0 0 13 10"><path d="M0 5h10M7 1.5L11 5L7 8.5" stroke="#ffffff" stroke-width="1.5" fill="none"/></svg>Home page</a>
    <a href="#"><svg viewBox="0 0 13 10"><path d="M0 5h10M7 1.5L11 5L7 8.5" stroke="#ffffff" stroke-width="1.5" fill="none"/></svg>About us</a>
    <a href="#"><svg viewBox="0 0 13 10"><path d="M0 5h10M7 1.5L11 5L7 8.5" stroke="#ffffff" stroke-width="1.5" fill="none"/></svg>Portfolio</a>
    <a href="#"><svg viewBox="0 0 13 10"><path d="M0 5h10M7 1.5L11 5L7 8.5" stroke="#ffffff" stroke-width="1.5" fill="none"/></svg>Solutions</a>
    <a href="#"><svg viewBox="0 0 13 10"><path d="M0 5h10M7 1.5L11 5L7 8.5" stroke="#ffffff" stroke-width="1.5" fill="none"/></svg>Contacts</a>
  </nav>

  <section class="column column--learn">
    <h2>Learn English today</h2>
    <p><span class="lead">Lorem ipsum dolor sit amet, contuer adipiscingelit</span>sed diamaccusantium doloremque laudantium, totam rem aperiam eaquep.</p>
    <p>Store veritatis et quasi architecto beatae vitae dicta sunt, explicabo nemo enim ipsam voluptatem, <a href="#">quia voluptas sit, aspernatur aut odit aut fugit.</a></p>
  </section>

  <section class="column column--about">
    <h2>About us</h2>
    <p><span class="lead">Lorem ipsum dolor sit amet, contuer adipiscingelit</span>sed diamaccusantium doloremque laudantium, totam rem aperiam eaquep. Store veritatis et quasi <a href="#">architecto beatae vitae dicta sunt</a>, explicabo nemo enim ipsam voluptatem, quia voluptas sit, aspernatur aut odit aut fugit.<br>Duis autem vel eum iriure dolor in hendrerit in vvdolore eu feugiat nulla facilisis at vero eros.</p>
  </section>

  <aside class="column column--news">
    <h2>Latest news</h2>
    <article class="news-item">
      <time>January 23th, 12</time>
      <p><b>Amet, consectetuer adipis cin</b>g elit sed diam nonummy nibh euismod tincidunt ut laoreet dolore magna aliquam erat <a href="#">volutpat.</a> Ut wisi enim ad minim veniamuis nostrud exerci tation ullamc orper</p>
      <a class="read-more" href="#">&bull; read more</a>
    </article>
    <article class="news-item">
      <time>September 22th, 12</time>
      <p><b>Amet, consectetuer adipis cin</b>g elit sed diam nonummy nibh euismod tincidunt ut laoreet dolore magna aliquam erat <a href="#">volutpat.</a></p>
      <a class="read-more" href="#">&bull; read more</a>
    </article>
  </aside>

  <footer class="site-footer">
    <p class="footer-copy">&copy; 2012 Leafline Studio. All rights reserved</p>
    <p class="footer-links"><a href="#">Terms of Use</a> &nbsp;|&nbsp; <a href="#">Privacy Statement</a></p>
    <div class="footer-art" role="img" aria-label="Dark green and black swirl ornament rising from the bottom edge"></div>
  </footer>

</div>
</body>
</html>
```